Design some Business Cards for my concierge service company

Hi Freelancers

I would need you to design some business cards for my company, the name of the company is (TheVelvetRope).

Please find the vector logo attached.

Here are the information that should appear on the business card:

Name: Mirela Dovanto
Job Tittle: CO-Founder
Email: info@thevelvetrope-example.com
Phone: +971 50 386 2719
Website: www.thevelvetrope-example.ae

Facebook/Twiter/instagram: TheVelvetRopeDubai

the main color are White, Black and gold. Keep in mind that I want the logo with gold foiling

For your information, the company will be offering concierge service for clubs in Dubai. So the business card should look very classy, proffesional and rich

Thanks for your entries

```html
<!DOCTYPE html>
<html lang="en">
<head>
<meta charset="utf-8">
<title>The Velvet Rope – Business Cards</title>
<link href="https://fonts.googleapis.com/css2?family=Roboto:wght@400;700&display=swap" rel="stylesheet">
<style>
  :root {
    --backdrop: #e4e5e7;
    --band-black: #1d1c1f;
    --card-brown: #3a201d;
    --stripe-brown: #6b4a3e;
    --gold: #c9a24e;
    --gold-soft: #8f6d33;
    --text-white: #ffffff;
    --text-muted: #cfc6c2;
    --rule: #8a7a74;
  }
  * { box-sizing: border-box; margin: 0; padding: 0; }
  html, body {
    width: 787px; height: 1200px; overflow: hidden;
    background: var(--backdrop);
    font-family: "Roboto", Arial, sans-serif;
  }
  .sheet {
    position: relative; width: 787px; height: 1200px;
    display: flex; flex-direction: column; align-items: center;
    justify-content: center; gap: 110px;
  }
  .card {
    position: relative; width: 620px; height: 354px;
    background: var(--card-brown);
    box-shadow: 0 6px 18px rgba(0,0,0,0.25);
    overflow: hidden;
  }
  .band {
    position: absolute; top: 0; bottom: 0; width: 108px;
    background: var(--band-black);
  }
  .band--left { left: 0; }
  .band--right { right: 0; }
  .stripe {
    position: absolute; top: 0; bottom: 0; width: 7px;
    background: var(--stripe-brown);
  }
  .stripe--left { left: 122px; }
  .stripe--right { right: 122px; }
  .ornament {
    position: absolute; width: 68px; height: 20px; border-radius: 10px;
    background: linear-gradient(90deg, var(--gold-soft), var(--gold), var(--gold-soft));
  }
  .ornament--left-top { left: 20px; top: 40px; }
  .ornament--left-bottom { left: 20px; bottom: 40px; }
  .ornament--right-top { right: 20px; top: 40px; }
  .ornament--right-bottom { right: 20px; bottom: 40px; }

  /* Front */
  .brand {
    position: absolute; left: 129px; right: 129px; top: 0; bottom: 0;
    display: flex; flex-direction: column; align-items: center; justify-content: center; gap: 14px;
  }
  .brand__mark {
    width: 54px; height: 54px; border-radius: 50%;
    border: 3px solid var(--gold);
  }
  .brand__name {
    color: var(--gold); font-weight: 700; font-size: 30px;
    letter-spacing: 1px; text-transform: uppercase;
  }
  .brand__city {
    color: var(--gold); font-weight: 700; font-size: 14px;
    letter-spacing: 6px; text-transform: uppercase;
  }

  /* Back */
  .contact {
    position: absolute; left: 150px; top: 70px; width: 320px;
    color: var(--text-white);
  }
  .contact__name { font-size: 22px; font-weight: 700; }
  .contact__title { font-size: 13px; color: var(--text-muted); margin-top: 6px; }
  .contact__rule { display: block; margin: 12px 0 16px; }
  .contact__list { list-style: none; }
  .contact__item {
    display: flex; align-items: center; gap: 12px;
    font-size: 12.5px; margin-bottom: 10px;
  }
  .contact__item svg { flex: none; }
  .social {
    position: absolute; right: 140px; bottom: 40px;
    display: flex; align-items: center; gap: 6px;
    color: var(--text-white); font-size: 13px;
  }
  .social__dot { width: 10px; height: 10px; border-radius: 50%; background: var(--text-white); }
  .social__handle { margin-left: 6px; }
</style>
</head>
<body>
<main class="sheet">
  <section class="card card--front" aria-label="Business card front">
    <div class="band band--left"></div>
    <div class="band band--right"></div>
    <div class="stripe stripe--left"></div>
    <div class="stripe stripe--right"></div>
    <div class="ornament ornament--left-top" role="img" aria-label="Gold scroll flourish"></div>
    <div class="ornament ornament--left-bottom" role="img" aria-label="Gold scroll flourish"></div>
    <div class="ornament ornament--right-top" role="img" aria-label="Gold scroll flourish"></div>
    <div class="ornament ornament--right-bottom" role="img" aria-label="Gold scroll flourish"></div>
    <div class="brand">
      <div class="brand__mark"></div>
      <div class="brand__name">The Velvet Rope</div>
      <div class="brand__city">Dubai</div>
    </div>
  </section>

  <section class="card card--back" aria-label="Business card back">
    <div class="band band--left"></div>
    <div class="band band--right"></div>
    <div class="stripe stripe--left"></div>
    <div class="stripe stripe--right"></div>
    <div class="ornament ornament--left-top" role="img" aria-label="Gold scroll flourish"></div>
    <div class="ornament ornament--left-bottom" role="img" aria-label="Gold scroll flourish"></div>
    <div class="ornament ornament--right-top" role="img" aria-label="Gold scroll flourish"></div>
    <div class="ornament ornament--right-bottom" role="img" aria-label="Gold scroll flourish"></div>
    <div class="contact">
      <h1 class="contact__name">Mirela Dovanto</h1>
      <p class="contact__title">CO-Founder</p>
      <svg class="contact__rule" width="300" height="10" viewBox="0 0 300 10">
        <polyline points="0,2 50,2 56,8 62,2 300,2" fill="none" stroke="var(--rule)" stroke-width="1"/>
      </svg>
      <ul class="contact__list">
        <li class="contact__item">
          <svg width="12" height="14" viewBox="0 0 12 14"><rect x="2" y="1" width="8" height="12" rx="1.5" fill="none" stroke="#fff" stroke-width="1.3"/><circle cx="6" cy="11" r="0.8" fill="#fff"/></svg>
          <span>+971 50 386 2719</span>
        </li>
        <li class="contact__item">
          <svg width="12" height="14" viewBox="0 0 12 14"><rect x="1" y="3" width="10" height="8" fill="none" stroke="#fff" stroke-width="1.3"/><polyline points="1,3 6,8 11,3" fill="none" stroke="#fff" stroke-width="1.1"/></svg>
          <span>info@thevelvetrope-example.com</span>
        </li>
        <li class="contact__item">
          <svg width="12" height="14" viewBox="0 0 12 14"><circle cx="6" cy="7" r="5" fill="none" stroke="#fff" stroke-width="1.3"/><ellipse cx="6" cy="7" rx="2" ry="5" fill="none" stroke="#fff" stroke-width="0.9"/><line x1="1" y1="7" x2="11" y2="7" stroke="#fff" stroke-width="0.9"/></svg>
          <span>www.thevelvetrope-example.ae</span>
        </li>
      </ul>
    </div>
    <div class="social">
      <span class="social__dot"></span>
      <span class="social__dot"></span>
      <span class="social__dot"></span>
      <span class="social__handle">TheVelvetRopeDubai</span>
    </div>
  </section>
</main>
</body>
</html>
```